CareShow482
Website Redesign
thanks PH :)
Hey EVERYONE! Sorry for the extended absence but we are now back, for at least a little while and want to see this completed! We will get feedback to those that have drafts but not ranked yet. Any new entries please get those in so we can get you feedback. If you have any questions or needs please let us know! Let's rock!
Trevor
Thank you everyone for participating. We have had an urgent situation arise that we will need some time away from work to complete. We have called Brandnest and have been advised upon return (6/14) we will most likely be extending the project at least one more 3 day time period to direct all the new participants and dial in the others. Thank you for your patience and god bless.
We are excited about the change in site submissions! There have been some new concepts that have caught our eye! Keep them coming!!
Thanks to everyone for your participation, we have extended the contest another 3 days with the hopes that some new and fresh ideas will grow. For clarification, we are looking for a fresh new concept for the website with a new landing page and internal page (both coded). We will then redevelop the rest of the website. Hope that helps!
We sincerely appreciate everyone's participation. We are still waiting for the creative side of those participating to come out. Thus far we are only seeing nearly the same format as our current site(other than #2). We are looking for something different, professional and inviting. We liked the picture background in #2 (just the wrong image for us). We liked tulap's use of a piece of the logo in other areas of the page (like next to the phone # in #29). Please keep trying! Thank you for reading!
You want to re-design your website only? or you want to include the re-development your code structure of your site, Please reply to our comments for clarifications. Thank You. : )
#4,#5,#6 still resemble too much of our current site. Try and take the elements and put your own creative twist! Please check the brief, and make sure you have the correct logo and navigation info. Thanks for submitting your hard work!
Hi PH,
Please check your private as well as my new concept.
Thanks!
Good initial start! There are elements in all of the current drafts that have potential. We want you to steer away from duplicating the look of our current site. Please incorporate your ideas into the new and improved design. We want our phone numbers somewhere near the top. And yes we are interested in having the 2 pages with coding.
I Found from Additional comments, means You are looking for a design with coding also?

```html
<!DOCTYPE html>
<html lang="en">
<head>
<meta charset="utf-8">
<title>CareShow482 – Home</title>
<link href="https://fonts.googleapis.com/css2?family=Arimo:wght@400;700&display=swap" rel="stylesheet">
<style>
:root{
  --blue:#1c63c4;
  --blue-dark:#0b3f93;
  --blue-light:#3f8ae6;
  --ink:#222;
  --grey-text:#8a8f96;
  --panel:#eceef0;
  --panel-border:#c9cdd2;
  --white:#fff;
}
*{box-sizing:border-box;margin:0;padding:0}
html,body{width:1200px;height:943px;overflow:hidden}
body{font-family:"Arimo",Arial,sans-serif;position:relative;background:#6d7770;color:var(--ink)}
.backdrop{position:absolute;left:0;top:0;width:1200px;height:700px;
  background:linear-gradient(90deg,#4d5d4a 0%,#8b9883 9%,#d9dcd8 14%,#f4f5f4 30%,#f7f7f7 70%,#d5d8d3 86%,#7e8c7a 92%,#3f4d3c 100%);}
.column{position:absolute;left:130px;top:0;width:950px;height:700px;
  background:linear-gradient(180deg,rgba(255,255,255,.9),rgba(246,246,246,.95));}
.logo{position:absolute;left:158px;top:30px;display:flex;align-items:center;gap:12px}
.logo-dot{width:40px;height:40px;border-radius:50%;background:var(--blue)}
.logo-name{font-size:40px;font-weight:700;color:#6c6f73;letter-spacing:-1px}
.phone-photo{position:absolute;left:768px;top:14px;width:112px;height:88px;border-radius:10px;
  background:linear-gradient(180deg,#6a6e73 0%,#3b3f44 60%,#2c2f33 100%)}
.call{position:absolute;left:892px;top:24px}
.call-label{font-size:27px;font-weight:700;color:#111}
.call-number{font-size:31px;font-weight:700;color:var(--blue);margin-top:2px}
.nav{position:absolute;left:471px;top:107px;width:594px;height:51px;border-radius:10px 10px 0 10px;
  background:linear-gradient(180deg,var(--blue-light),var(--blue-dark));display:flex;align-items:center;justify-content:space-evenly;
  box-shadow:0 3px 6px rgba(0,0,0,.3)}
.nav a{color:var(--white);text-decoration:none;font-size:14px}
.nav .sep{color:#9cc0f0;font-size:14px}
.panel{position:absolute;background:linear-gradient(180deg,#f6f7f8,var(--panel));border:1px solid var(--panel-border);border-radius:14px;box-shadow:0 2px 6px rgba(0,0,0,.15)}
.welcome{left:145px;top:180px;width:620px;height:325px;padding:16px 22px}
.welcome h1{display:flex;align-items:center;gap:10px;font-size:21px;font-weight:400;color:var(--blue);margin-bottom:10px}
.welcome h1 .mark{width:28px;height:28px;border-radius:50%;background:var(--blue)}
.welcome p{font-size:10.5px;line-height:14px;color:var(--grey-text);margin-bottom:14px}
.quote{left:810px;top:186px;width:235px;height:242px;padding:12px 14px}
.quote h2{font-size:17px;font-weight:400;color:#9a9ea4;border-bottom:1px solid var(--panel-border);padding-bottom:8px;margin-bottom:10px}
.field{display:flex;align-items:center;margin-bottom:9px}
.field label{font-size:11px;width:58px;color:#333}
.field span{flex:1;height:18px;background:var(--white);border:1px solid #c6c9cd}
.field.tall{align-items:flex-start}
.field.tall span{height:62px}
.submit{display:block;margin:4px 0 0 auto;width:56px;height:18px;font-size:10px;border:1px solid #aaa;border-radius:3px;background:linear-gradient(#fff,#ddd);text-align:center;line-height:16px;color:#333}
.social{position:absolute;left:866px;top:452px;display:flex;gap:14px}
.social span{width:42px;height:42px;border-radius:8px;background:linear-gradient(180deg,#4a8fe0,#1c5aa8);box-shadow:0 2px 3px rgba(0,0,0,.3)}
.feature{position:absolute;top:530px;width:290px;height:158px;border-radius:22px;overflow:hidden;
  background:linear-gradient(180deg,#fbfbfb,#e3e5e7);border:1px solid var(--panel-border);box-shadow:0 2px 6px rgba(0,0,0,.18);text-align:center}
.feature .accent{position:absolute;left:0;top:0;width:64px;height:100%;
  background:linear-gradient(90deg,rgba(31,98,192,.55) 0%,rgba(31,98,192,.2) 55%,rgba(31,98,192,0) 100%)}
.feature h3{position:relative;margin:30px 16px 0 72px;font-size:19px;font-weight:400;color:#7d8187;white-space:nowrap}
.feature p{position:relative;font-size:10px;line-height:12px;color:#333;margin:3px 22px 0 78px;text-align:center}
.play{position:absolute;left:50%;bottom:18px;transform:translateX(-50%);width:78px;height:14px;border-radius:3px;background:linear-gradient(#4d9bf0,#1f62c0);color:#fff;font-size:7px;line-height:14px;font-weight:700}
.band{position:absolute;left:0;top:693px;width:1200px;height:250px;background:linear-gradient(180deg,#c9cbce 0%,#a2a6aa 40%,#8c9094 100%)}
.card{position:absolute;top:713px;width:296px;height:167px;border-radius:12px;overflow:hidden;border:3px solid #eef0f2;box-shadow:0 3px 8px rgba(0,0,0,.35)}
.card h4{position:absolute;left:0;top:0;height:34px;padding:0 26px 0 12px;line-height:34px;border-radius:0 0 18px 0;
  background:linear-gradient(180deg,var(--blue-light),var(--blue-dark));color:#fff;font-size:16px;font-weight:700;z-index:1}
.card .photo{position:absolute;inset:0}
.footer{position:absolute;top:906px;left:0;width:1200px;text-align:center;font-size:10px;color:#eef0f2}
.footer b{color:#cfe0ff;font-weight:400}
</style>
</head>
<body>
<div class="backdrop" role="img" aria-label="Blurred photo of a city street with trees and passing ambulance"></div>
<div class="column"></div>

<header>
  <div class="logo"><span class="logo-dot"></span><span class="logo-name">CareShow482</span></div>
  <div class="phone-photo" role="img" aria-label="Photo of a desk telephone"></div>
  <div class="call"><div class="call-label">Call Us Now</div><div class="call-number">0000 000 00</div></div>
  <nav class="nav">
    <a href="#">Home</a><span class="sep">|</span><a href="#">Our Services</a><span class="sep">|</span><a href="#">FAQ's</a><span class="sep">|</span><a href="#">About Us</a><span class="sep">|</span><a href="#">Contact Us</a><span class="sep">|</span><a href="#">Testimonials</a>
  </nav>
</header>

<main>
  <section class="panel welcome">
    <h1><span class="mark"></span>Welcome to CareShow Events</h1>
    <p>Lorem ipsum dolor sit amet, consectetur adipiscing elit. Cras condimentum laoreet leo sit amet tristique. Aenean feugiat auctor elit. Sed eu ullamcorper dui. Sed sed erat tortor, a vestibulum metus. Etiam blandit, magna vitae convallis lobortis, velit erat malesuada nisi, in laoreet mauris sapien sit amet urna. Sed diam libero, rhoncus at laoreet eu, porta at arcu. Quisque auctor, odio et viverra porttitor, tellus turpis porttitor orci, sit amet vestibulum urna mauris vitae lorem. Duis diam nulla, pellentesque a suscipit id, ultricies sed nulla.</p>
    <p>Nulla vitae quam nisi. Suspendisse vitae lobortis eros. Morbi eleifend, diam eget fringilla rutrum, velit diam elementum lacus, id condimentum orci justo ac eros. Praesent tempor neque id orci bibendum luctus. Nulla facilisi. Phasellus adipiscing viverra tristique.</p>
    <p>Etiam in dolor sit amet neque vehicula feugiat. Vestibulum rutrum, tellus porttitor venenatis rhoncus, eros eros tristique elit, eu porttitor lacus purus sed sed. Morbi et tellus nibh. Nulla accumsan, mauris non molestie sagittis, ex velit blandit orci, vitae ornare est odio sit amet justo.</p>
  </section>

  <aside class="panel quote">
    <h2>Quote Request</h2>
    <div class="field"><label>Name</label><span></span></div>
    <div class="field"><label>Phone</label><span></span></div>
    <div class="field"><label>Email</label><span></span></div>
    <div class="field tall"><label>Message</label><span></span></div>
    <span class="submit">Submit</span>
  </aside>

  <div class="social"><span></span><span></span><span></span></div>

  <article class="feature" style="left:145px">
    <div class="accent" role="img" aria-label="Decorative blue curve"></div>
    <h3>Watch Intro</h3>
    <p>for adipiscing elit. Cras condimentum laoreet leo sit amet tristique. Aenean feugiat auctor elit. Sed eu ullamcorper</p>
    <span class="play">CLICK TO PLAY</span>
  </article>
  <article class="feature" style="left:460px">
    <div class="accent" role="img" aria-label="Decorative blue curve"></div>
    <h3>Watch Latest Videos</h3>
    <p>for adipiscing elit. Cras condimentum laoreet leo sit amet tristique. Aenean feugiat auctor elit. Sed eu ullamcorper</p>
    <span class="play">CLICK TO PLAY</span>
  </article>
  <article class="feature" style="left:775px">
    <div class="accent" role="img" aria-label="Decorative blue curve"></div>
    <h3>Watch Testimonials</h3>
    <p>for adipiscing elit. Cras condimentum laoreet leo sit amet tristique. Aenean feugiat auctor elit. Sed eu ullamcorper</p>
    <span class="play">CLICK TO PLAY</span>
  </article>
</main>

<section class="band"></section>
<article class="card" style="left:138px">
  <h4>Basic Life Support</h4>
  <div class="photo" role="img" aria-label="Photo of a hospital building entrance" style="background:linear-gradient(180deg,#8fb6de 0%,#c3cfd8 40%,#8b5a48 70%,#6f7b62 100%)"></div>
</article>
<article class="card" style="left:451px">
  <h4>Advanced Life Support</h4>
  <div class="photo" role="img" aria-label="Photo of laboratory test tubes and pipette in blue light" style="background:linear-gradient(135deg,#0d3f8a 0%,#2f86d6 45%,#9fd2f5 75%,#1a4f9c 100%)"></div>
</article>
<article class="card" style="left:764px">
  <h4>Medical Staffing</h4>
  <div class="photo" role="img" aria-label="Photo of a stethoscope resting on a medical chart" style="background:linear-gradient(135deg,#e9ecef 0%,#c9ced3 50%,#8f969d 100%)"></div>
</article>

<footer class="footer">Copyright © 2012 <b>CareShow482</b>. All rights reserved.</footer>
</body>
</html>
```